Gourmet Restaurant take out menu

We need a take out menu design that is trendy for a casual upscale Italian restaurant with a vast menu. This menu must be able to be 4 color and reproducible in large quantities to be bulked mailed or inserted into a daily paper. It must also maintain a theme that can be crossed over to our in house dining menu and specials menu.
OUR WEBSITE:
www.velmorabistrohouse.example
For the content, go to the Menu section of our website. We are interested in the design scheme and a template to use.
Target Market(s)
families, sinle individuals seeking take out meals and delivery
Industry/Entity Type
Restaurant

```html
<!DOCTYPE html>
<html lang="en">
<head>
<meta charset="utf-8">
<title>Gourmet Pizza &amp; Subs Take Out Menu</title>
<link rel="stylesheet" href="https://fonts.googleapis.com/css2?family=Pinyon+Script&family=Cormorant+SC:wght@500;600&family=Catamaran:wght@500&display=swap">
<style>
  :root {
    --orange: #d2591c;
    --orange-light: #f2a25a;
    --cream: #f9ecd6;
    --peach: #f1cfad;
    --ink: #1f1a17;
    --brown: #3b2b23;
  }
  * { margin: 0; padding: 0; box-sizing: border-box; }
  html, body { width: 929px; height: 1200px; overflow: hidden; }
  body {
    position: relative;
    background: radial-gradient(ellipse at 35% 40%, var(--cream) 0%, #f6e2c6 45%, var(--peach) 100%);
    color: var(--ink);
    font-family: "Catamaran", sans-serif;
  }
  .top-band {
    position: absolute; left: 0; top: 0; width: 929px; height: 56px;
    background: var(--orange);
  }
  .top-band-glow {
    position: absolute; left: 0; top: 56px; width: 929px; height: 15px;
    background: linear-gradient(90deg, #f3b57a 0%, #fbe6cf 50%, #f2a25a 100%);
  }
  .frame { position: absolute; left: 0; top: 0; }
  .section-title {
    position: absolute; left: 0; width: 929px; text-align: center;
    font-family: "Pinyon Script", cursive; font-size: 48px; color: var(--ink);
    line-height: 1;
  }
  .pizza-title { top: 90px; }
  .pizza-sizes {
    position: absolute; top: 148px; left: 0; width: 929px; text-align: center;
    font-size: 14.5px; line-height: 20px;
  }
  .menu-column {
    position: absolute; width: 420px; text-align: center;
    font-size: 14.5px; line-height: 21px;
  }
  .pizza-left { left: 38px; top: 210px; }
  .pizza-right { left: 478px; top: 210px; }
  .item-name {
    font-family: "Cormorant SC", serif; font-weight: 500; font-size: 18px;
    color: var(--brown); letter-spacing: 0.3px;
  }
  .item-name .price { font-family: "Catamaran", sans-serif; font-size: 14.5px; color: var(--ink); margin-left: 4px; }
  .toppings {
    position: absolute; top: 612px; left: 0; width: 929px; text-align: center;
    font-size: 14.5px; line-height: 20px;
  }
  .subs-title { top: 740px; left: 0; font-size: 50px; }
  .subs-divider {
    position: absolute; left: 466px; top: 791px; width: 1px; height: 323px;
    background: var(--orange);
  }
  .subs-list {
    position: absolute; width: 420px; top: 763px; text-align: center;
    font-family: "Cormorant SC", serif; font-weight: 500; font-size: 19px;
    line-height: 24px; color: var(--brown); list-style: none;
  }
  .subs-list .price { font-family: "Catamaran", sans-serif; font-size: 14.5px; color: var(--ink); margin-left: 4px; }
  .subs-hot { left: 28px; }
  .subs-right { left: 485px; }
</style>
</head>
<body>
  <div class="top-band"></div>
  <div class="top-band-glow"></div>

  <svg class="frame" width="929" height="1200" viewBox="0 0 929 1200" aria-hidden="true">
    <defs>
      <linearGradient id="frameStroke" x1="0" y1="0" x2="1" y2="1">
        <stop offset="0" stop-color="#d2591c"/>
        <stop offset="0.5" stop-color="#f6c48e"/>
        <stop offset="1" stop-color="#e57a2b"/>
      </linearGradient>
    </defs>
    <g fill="none" stroke="url(#frameStroke)">
      <path stroke-width="3" d="M38 84 H896 V96 H908 V696 H896 V708 H38 V696 H26 V96 H38 Z"/>
      <path stroke-width="1.2" d="M44 90 H890 V102 H902 V690 H890 V702 H44 V690 H32 V102 H44 Z"/>
      <path stroke-width="3" d="M40 723 H900 V735 H912 V1144 H900 V1156 H40 V1144 H28 V735 H40 Z"/>
      <path stroke-width="1.2" d="M46 729 H894 V741 H906 V1138 H894 V1150 H46 V1138 H34 V741 H46 Z"/>
    </g>
  </svg>

  <h1 class="section-title pizza-title">Gourmet Pizza</h1>
  <p class="pizza-sizes">10” Individual, 12” Medium, 16” Large<br>Pizza By The Slice - Plain 1.99, Veggie 2.99</p>

  <div class="menu-column pizza-left">
    <div class="item-name">Plain Cheese <span class="price">8.99/11.99/12.99</span></div>
    <div class="item-name">Traditional White</div>
    <p>Olive oil, garlic, mozzarella cheese. 8.59/11.59/13.99</p>
    <div class="item-name">Chicken Bacon Ranch</div>
    <p>Garlic chicken, bacon, pepperjack and cheddar cheese, red onions, diced tomatoes, drizzle of ranch dressing. 10.99/14.99/16.99</p>
    <div class="item-name">Bronx Bomber</div>
    <p>Sausage, prosciutto ham, oregano, crumbled bleu and mozzarella cheese. 11.99/14.99/16.99</p>
    <div class="item-name">Buffalo Chicken</div>
    <p>Buffalo sauce, chicken, mozzarella cheese, side of bleu cheese dressing. 10.99/14.99/16.99</p>
    <div class="item-name">Gourmet Special</div>
    <p>Pepperoni, sausage, bell peppers, mushrooms, onion, mozzarella cheese. 12.99/16.99/18.99</p>
    <div class="item-name">Margarita</div>
    <p>Fresh basil, tomato, buffalo mozzarella cheese.<br>8.99/11.99/13.99</p>
  </div>

  <div class="menu-column pizza-right">
    <div class="item-name">Roasted Vegetable</div>
    <p>Eggplant, red and yellow peppers, onions, artichokes, Kalamata olives, tomatoes, mozzarella cheese.</p>
    <div class="item-name">Veggie Lover</div>
    <p>Olive oil, garlic, broccoli, spinach, tomato, mozzarella cheese. 11.99/14.99/16.99</p>
    <div class="item-name">Sweet Hawaiian</div>
    <p>Pineapple, tomatoes, ham, mozzarella cheese.<br>11.99/14.99/16.99</p>
    <div class="item-name">Spinach and Artichoke</div>
    <p>Spinach, artichoke hearts, basil, mozzarella, parmesan cheese. 8.99/11.99/12.99</p>
    <div class="item-name">Philly Cheese Steak</div>
    <p>Philly steak, green peppers, onions, provolone, American cheese. 11.99/14.99/16.99</p>
    <div class="item-name">Grandma’s Pie</div>
    <p>Thin crust pizza topped with mozzarella, tomato sauce, buffalo mozzarella, fresh basil, olive oil. (1 Size) 14.99</p>
  </div>

  <div class="toppings">
    <div class="item-name">Extra Toppings <span class="price">for 1.99</span></div>
    <p>Ham • Broccoli • Extra Cheese • Tomatoes Hot Or Sweet Peppers<br>• Roasted Peppers • Pepperoni • Spinach • Italian Sausage • Black Olives • Green Peppers<br>• Mushrooms • Onions • Anchovies • Grilled Chicken • Meatball Bacon And Ricotta 3.00</p>
  </div>

  <h2 class="section-title subs-title">Subs</h2>
  <div class="subs-divider"></div>

  <ul class="subs-list subs-hot">
    <li>— Hot —</li>
    <li>Cheesesteak <span class="price">6.59</span></li>
    <li>Bacon Cheesesteak <span class="price">7.59</span></li>
    <li>Steak Sub <span class="price">6.29</span></li>
    <li>Chicken Parmigiana <span class="price">6.99</span></li>
    <li>Pepper, Egg, &amp; Cheese <span class="price">6.29</span></li>
    <li>Pizza Cheesesteak <span class="price">6.99</span></li>
    <li>Meatball Parmigiana <span class="price">6.99</span></li>
    <li>Mushroom Cheesesteak <span class="price">6.99</span></li>
    <li>Veal Parmigiana <span class="price">7.99</span></li>
    <li>Pepper Cheesesteak <span class="price">6.99</span></li>
    <li>Vegetarian with Cheese <span class="price">6.59</span></li>
    <li>Eggplant Parmigiana <span class="price">6.59</span></li>
    <li>Chicken Cheesesteak <span class="price">6.99</span></li>
    <li>Sausage Parmigiana <span class="price">7.59</span></li>
  </ul>

  <ul class="subs-list subs-right">
    <li>Grilled Chicken <span class="price">6.59</span></li>
    <li>Cheeseburger Sub <span class="price">7.59</span></li>
    <li>Chicken Cacciatore <span class="price">7.59</span></li>
    <li>Steak Cacciatore <span class="price">7.59</span></li>
    <li>Sausage, Peppers, &amp; Onion <span class="price">6.99</span></li>
    <li>— Cold —</li>
    <li>Regular Italian <span class="price">6.59</span></li>
    <li>Tuna <span class="price">6.59</span></li>
    <li>Roast Beef <span class="price">7.59</span></li>
    <li>Imported Ham <span class="price">6.59</span></li>
    <li>Roast Turkey <span class="price">6.99</span></li>
    <li>Provolone <span class="price">6.59</span></li>
    <li>Capicola, Salami, &amp; Provolone <span class="price">6.99</span></li>
    <li>Chicken Salad <span class="price">6.99</span></li>
  </ul>
</body>
</html>
```